We need a new business card that reflects who we are. Professional, classy, modern, and service ori

We need a business card design for a window coverings design company in Kansas City called Bright Lane Interiors. We offer professional, modern, and high quality window covering products. We are looking to portray an image of a big, national franchise. We are a 5 location (with showrooms) business with 10 professional designers and 4 professional installers. These cards will be used with Thank you cards, given to realtors, and asked for referrals with.

Target Market(s)

Kansas City

Industry/Entity Type

Business

Contact Information for Business Card

We would like our card to look clean and simple on the front, featuring our logo and Marlow Fenwick's. Our designers' phone numbers and emails should be displayed as well as their title.

Font styles to use
Sans Serif

Colors

Designer to choose colors to be used in the design.

Requirements
Must have
• Front - Logos, name, phone number, email address
• Back - Showroom locations, social media? Appt date/time?
Nice to have
• I would like a clean and modern look (not contemporary. I like a white background, but I am open to ideas. Looking for a "National chain" look for a small business.
Should not have
• Too much busyness.

```html
<!DOCTYPE html>
<html lang="en">
<head>
<meta charset="utf-8">
<title>Bright Lane Interiors — Business Card</title>
<link rel="stylesheet" href="https://fonts.googleapis.com/css2?family=Lato:wght@400;700&family=Libre+Baskerville:wght@400;700&display=swap">
<style>
  :root {
    --page-bg: #e9e7e4;
    --card-bg: #ffffff;
    --ink: #1a1a1a;
    --accent-red: #c8353b;
    --muted-grey: #8c8c8c;
    --rule-grey: #9a9a9a;
    --partner-orange: #ef7f1a;
    --card-shadow: 0 10px 28px rgba(0,0,0,.18);
  }
  * { box-sizing: border-box; margin: 0; padding: 0; }
  html, body { width: 1200px; height: 900px; overflow: hidden; }
  body {
    background: var(--page-bg);
    font-family: "Lato", Arial, sans-serif;
    color: var(--ink);
    position: relative;
  }
  .card {
    position: absolute;
    top: 296px;
    width: 540px;
    height: 308px;
    background: var(--card-bg);
    box-shadow: var(--card-shadow);
  }
  .card--front { left: 40px; }
  .card--back { left: 620px; }

  /* brand block */
  .brand { position: absolute; }
  .brand__name {
    display: flex; align-items: center; gap: 10px;
    font-family: "Lato", Arial, sans-serif;
    font-weight: 700;
    font-size: 25px;
    color: var(--ink);
    letter-spacing: .2px;
  }
  .brand__mark {
    width: 18px; height: 18px;
    background: var(--accent-red);
    flex: none;
  }
  .brand__tagline {
    font-family: "Libre Baskerville", Georgia, serif;
    font-size: 11.5px;
    margin-top: 6px;
    padding-left: 28px;
    color: var(--ink);
  }
  .card--front .brand { right: 36px; top: 92px; }

  /* contact block */
  .contact { position: absolute; left: 40px; bottom: 40px; }
  .contact__name {
    font-family: "Libre Baskerville", Georgia, serif;
    font-weight: 700;
    font-size: 19px;
    letter-spacing: .5px;
  }
  .contact__first { color: var(--accent-red); }
  .contact__title { font-size: 16px; margin-top: 2px; }
  .contact__list { list-style: none; margin-top: 12px; }
  .contact__item {
    display: flex; align-items: center; gap: 9px;
    font-size: 16px; line-height: 25px;
  }
  .contact__icon { width: 14px; height: 14px; flex: none; }

  /* back */
  .card--back .brand { left: 40px; top: 46px; }
  .card--back .brand__name { font-size: 22px; }
  .card--back .brand__tagline { font-size: 10.5px; }
  .partner {
    position: absolute; right: 36px; top: 30px;
    display: flex; flex-direction: column; align-items: center; gap: 6px;
  }
  .partner__mark {
    width: 54px; height: 54px; border-radius: 50%;
    background: var(--partner-orange);
  }
  .partner__name {
    font-size: 12px; font-weight: 700; color: #3a4a66; text-align: center; line-height: 1.2;
  }
  .showrooms {
    position: absolute; left: 40px; right: 36px; top: 132px;
    text-align: center;
  }
  .showrooms__heading {
    font-size: 14px; letter-spacing: 1px; color: var(--muted-grey);
  }
  .showrooms__rule {
    border: 0; border-top: 1px solid var(--rule-grey); margin: 8px 0 10px;
  }
  .showrooms__list {
    list-style: none; display: flex; justify-content: center; flex-wrap: wrap;
    gap: 6px 0;
  }
  .showrooms__item { color: var(--accent-red); font-size: 14.5px; }
  .showrooms__item + .showrooms__item::before {
    content: ""; display: inline-block; width: 6px; height: 6px; border-radius: 50%;
    background: var(--muted-grey); margin: 0 10px 2px; vertical-align: middle;
  }
  .social {
    display: flex; justify-content: center; gap: 4px; margin-top: 10px;
  }
  .social__dot { width: 15px; height: 15px; border-radius: 50%; background: #5f6f86; }
  .appointment {
    position: absolute; left: 40px; right: 36px; bottom: 30px;
    display: flex; gap: 24px; justify-content: center;
    font-size: 15px; font-weight: 700;
  }
  .appointment__field { display: flex; align-items: flex-end; gap: 4px; }
  .appointment__line { display: inline-block; width: 150px; border-bottom: 1.5px solid var(--ink); height: 14px; }
</style>
</head>
<body>

  <section class="card card--front" aria-label="Business card front">
    <div class="brand">
      <div class="brand__name"><span class="brand__mark"></span>Bright Lane Interiors</div>
      <div class="brand__tagline">Blinds, Shades, Shutters, Draperies &amp; Decor</div>
    </div>

    <div class="contact">
      <div class="contact__name"><span class="contact__first">DANIEL</span> REYES</div>
      <div class="contact__title">Managing Director</div>
      <ul class="contact__list">
        <li class="contact__item">
          <svg class="contact__icon" viewBox="0 0 16 16" aria-hidden="true"><path fill="#c8353b" d="M3.6 1.5l2.3 2.6-1.3 1.8c.9 1.9 2.4 3.4 4.3 4.3l1.8-1.3 2.6 2.3-1.2 2.3C7 13.4 2.6 9 2.1 3.1z"/></svg>
          444 555 0192
        </li>
        <li class="contact__item">
          <svg class="contact__icon" viewBox="0 0 16 16" aria-hidden="true"><rect x="1" y="3" width="14" height="10" fill="#c8353b"/><path d="M1.5 3.5L8 9l6.5-5.5" fill="none" stroke="#fff" stroke-width="1.3"/></svg>
          info@brightlaneinteriors.com
        </li>
      </ul>
    </div>
  </section>

  <section class="card card--back" aria-label="Business card back">
    <div class="brand">
      <div class="brand__name"><span class="brand__mark"></span>Bright Lane Interiors</div>
      <div class="brand__tagline">Blinds, Shades, Shutters, Draperies &amp; Decor</div>
    </div>

    <div class="partner">
      <span class="partner__mark"></span>
      <span class="partner__name">Marlow Fenwick<br>Gallery</span>
    </div>

    <div class="showrooms">
      <div class="showrooms__heading">SHOWROOM LOCATIONS</div>
      <hr class="showrooms__rule">
      <ul class="showrooms__list">
        <li class="showrooms__item">Location 1</li>
        <li class="showrooms__item">Location 2</li>
        <li class="showrooms__item">Location 3</li>
        <li class="showrooms__item">Location 4</li>
        <li class="showrooms__item">Location 5</li>
      </ul>
      <div class="social" aria-label="Social media">
        <span class="social__dot"></span><span class="social__dot"></span><span class="social__dot"></span><span class="social__dot"></span>
      </div>
    </div>

    <div class="appointment">
      <span class="appointment__field">DATE<span class="appointment__line"></span></span>
      <span class="appointment__field">TIME<span class="appointment__line"></span></span>
    </div>
  </section>

</body>
</html>
```